The World Most Wanted Eyelahes

1. We need a web design for a new company based in California, USA
2. We are the manufacturer for 100% human hair eyelashes,
made in Indonesia.
3. We recently launched "Tapered Eyelashes" with human hair.
Currently, none of the people carried Tapered eyelash.
4. We would like to see designs that use the 4 different colors that match with my products as "Four Seasons" concepts.
5. We prefer to follow www.velkro.com style, like professional website.
6. Focus on products as a manufacturer, therefore, all wholesaler and retailer copy and paste to their marketing tools.
7. Need bilingual English and Spanish.
8. Easy to link with social media.

Target Market(s)

United States and Central/South America.

Industry/Entity Type

Hair

Number of Pages Required

5+ page

Requirements
Must have
• 1. Details of Products with image.
• 2. Hottest/Newest Items "Tapered in 100% Human Hair"
• 3. Store Page
Nice to have
• 1. My competitors is Morvine Eyelash. http://www.morvinelashes.com/
• Please follow the concepts of it.
• 2. www.Velkro.com: They have great products detail on the website.
• i would like to focus on "Tapered" for new styles of the eyelash.
• 3. I want to visitors can write down the "Reviews" in every single product.
• Please check the www.QELCosmetics.com.
Should not have
• It's not salon/Shop for the beauty.
• No need an appointment.
• We are the manufacturer of the eyelash.

```html
<!DOCTYPE html>
<html lang="en">
<head>
<meta charset="utf-8">
<title>Aurelle — Tapered Eyelashes</title>
<link rel="stylesheet" href="https://fonts.googleapis.com/css2?family=Marcellus&family=Roboto+Condensed:wght@300;400&family=Merriweather:wght@400&family=Roboto:wght@400;500&display=swap">
<style>
:root{
  --bg-dark:#271410;
  --nav:#1c0f0b;
  --gold:#c9a46a;
  --gold-light:#e2c089;
  --gold-btn:#c79a55;
  --text-light:#efe6dc;
  --reviews:#6b4530;
  --footer:#2a1712;
  --rule:#4a3026;
  --social:#d6c3a5;
}
*{margin:0;padding:0;box-sizing:border-box}
html,body{width:1200px;height:1115px;overflow:hidden;background:var(--bg-dark)}
body{position:relative;font-family:"Roboto",sans-serif;color:var(--text-light)}
.abs{position:absolute}

/* header */
.site-header{position:absolute;left:0;top:0;width:1200px;height:110px;background:var(--bg-dark)}
.brand{position:absolute;left:145px;top:24px;font-family:"Marcellus",serif;font-size:54px;color:var(--gold);letter-spacing:1px;line-height:1}
.shipping{position:absolute;left:615px;top:30px;width:137px;height:34px;border:1px solid #5a3a26;border-radius:3px;display:flex;align-items:center;gap:7px;padding-left:7px}
.shipping span{font-size:9.5px;line-height:12px;color:var(--gold)}
.top-links{position:absolute;top:30px;left:772px;display:flex;align-items:center;font-size:12px;color:var(--gold)}
.top-links a{color:inherit;text-decoration:none;padding:0 14px;border-right:1px solid #5a3a26;line-height:16px}
.top-links a:first-child{padding-left:8px}
.top-links .lang{color:#fff;font-weight:500;border:none;padding:0 6px}
.top-links .lang.first{padding-left:14px}
.search{position:absolute;left:877px;top:64px;width:160px;height:23px;background:#fff;border:1px solid #888;font-size:13px;color:#333;padding:3px 6px}
.search-btn{position:absolute;left:1033px;top:59px;width:29px;height:29px;border-radius:50%;background:var(--gold-btn);border:2px solid #e8d2a8}

/* nav */
.main-nav{position:absolute;left:0;top:110px;width:1200px;height:39px;background:var(--nav)}
.main-nav a{position:absolute;top:0;height:39px;line-height:41px;text-align:center;font-family:"Roboto Condensed",sans-serif;font-size:15px;color:#fff;text-decoration:none;border-left:1px solid #3d2a22}
.main-nav a.active{color:var(--gold-light);border-bottom:3px solid #d48f3e}
.main-nav .last{position:absolute;left:1069px;top:0;width:1px;height:39px;background:#3d2a22}

/* hero */
.hero{position:absolute;left:0;top:149px;width:1200px;height:603px;background:radial-gradient(ellipse at 22% 55%,#a86a22 0%,#6a3a16 30%,#3a1e0e 60%,#120805 100%)}
.hero-photo{position:absolute;left:0;top:0;width:500px;height:603px;background:radial-gradient(ellipse at 30% 42%,#d9a46c 0%,#b07840 28%,#7d4a1e 55%,rgba(90,48,19,0) 85%),radial-gradient(ellipse at 5% 80%,#f3c063 0%,rgba(243,192,99,0) 35%)}
.hero-title{position:absolute;left:470px;top:116px;width:566px;font-family:"Marcellus",serif;font-weight:400;color:#fff;text-shadow:0 2px 4px rgba(0,0,0,.6)}
.hero-title .l1{display:block;text-align:center;font-size:52px;letter-spacing:1px;line-height:60px}
.hero-title .l2{display:block;text-align:right;font-size:44px;letter-spacing:1px;line-height:52px}
.hero-copy{position:absolute;left:484px;top:247px;width:547px;height:168px;background:rgba(20,10,6,.45);padding:12px 20px;font-family:"Roboto Condensed",sans-serif;font-weight:300;font-size:22px;line-height:35px;color:#f3ece4}

/* seasons */
.white-band{position:absolute;left:0;top:752px;width:1200px;height:159px;background:#fff}
.season{position:absolute;top:752px;width:234px;height:159px;text-align:center}
.season .caption{position:absolute;left:0;top:72px;width:234px;font-family:"Merriweather",serif;font-size:22px;line-height:33px;color:#fff;text-shadow:0 1px 3px rgba(0,0,0,.35);white-space:nowrap;letter-spacing:-.2px}
.season-thumb{position:absolute;top:684px;width:132px;height:132px;border-radius:50%;background:rgba(255,255,255,.35);padding:7px}
.season-thumb div{width:118px;height:118px;border-radius:50%;border:2px solid #fff}
.cart{position:absolute;top:893px;width:38px;height:38px;border-radius:50%;background:#fff;display:flex;align-items:center;justify-content:center}

.reviews-band{position:absolute;left:0;top:911px;width:1200px;height:83px;background:#301a13}
.review-btn{position:absolute;top:948px;width:152px;height:25px;background:var(--reviews);border-radius:2px;font-family:"Roboto Condensed",sans-serif;font-size:11px;color:#f3e6d6;text-align:center;line-height:25px}
.review-btn::before{content:"";position:absolute;left:70px;top:-6px;border:6px solid transparent;border-top:0;border-bottom-color:var(--reviews)}

/* footer */
.site-footer{position:absolute;left:0;top:994px;width:1200px;height:121px;background:var(--footer)}
.news-label{position:absolute;left:135px;top:23px;font-size:16px;color:#f2ebe3}
.email{position:absolute;left:306px;top:18px;width:215px;height:32px;border:1px solid #8a6a4a;border-radius:3px;font-size:12px;font-weight:500;color:#fff;padding:9px 10px}
.subscribe{position:absolute;left:532px;top:18px;width:92px;height:32px;background:var(--gold-btn);border:1px solid #e0c08a;border-radius:3px;font-size:12px;font-weight:500;color:#fff;text-align:center;line-height:30px}
.follow{position:absolute;left:819px;top:23px;font-size:16px;color:#f2ebe3}
.social{position:absolute;top:20px;width:27px;height:27px;border-radius:50%;border:1.5px solid var(--social);display:flex;align-items:center;justify-content:center}
.rule{position:absolute;left:131px;top:70px;width:938px;height:1px;background:var(--rule)}
.copyright{position:absolute;left:0;top:91px;width:1200px;text-align:center;font-size:12.5px;color:#efe6dc}
</style>
</head>
<body>

<header class="site-header">
  <div class="brand">AURELLE</div>
  <div class="shipping">
    <svg width="28" height="18" viewBox="0 0 28 18" aria-hidden="true"><rect x="1" y="3" width="16" height="10" fill="none" stroke="#c9a46a" stroke-width="1.4"/><path d="M17 6h6l4 4v3h-10z" fill="none" stroke="#c9a46a" stroke-width="1.4"/><circle cx="6" cy="15" r="2" fill="#c9a46a"/><circle cx="22" cy="15" r="2" fill="#c9a46a"/></svg>
    <span>free shipping on all<br>orders over $25</span>
  </div>
  <nav class="top-links">
    <a>MY ACCOUNT</a><a>LOGIN</a><a>CART(0)</a><a class="lang first">EN</a><a class="lang">ES</a>
  </nav>
  <div class="search">Search Here</div>
  <div class="search-btn">
    <svg width="25" height="25" viewBox="0 0 25 25" aria-hidden="true"><path d="M8 12.5h7M13 9.5l3.5 3-3.5 3z" stroke="#fff" stroke-width="2" fill="#fff"/></svg>
  </div>
</header>

<nav class="main-nav">
  <a class="active" style="left:131px;width:115px">HOME</a>
  <a style="left:246px;width:119px">WHAT'S NEW</a>
  <a style="left:365px;width:93px">FACE</a>
  <a style="left:458px;width:92px">EYES</a>
  <a style="left:550px;width:88px">LIPS</a>
  <a style="left:638px;width:97px">NAILS</a>
  <a style="left:735px;width:91px">BODY</a>
  <a style="left:826px;width:91px">SETS</a>
  <a style="left:917px;width:152px">ACCESSORIES</a>
  <span class="last"></span>
</nav>

<section class="hero">
  <div class="hero-photo" role="img" aria-label="Model with golden makeup and long tapered lashes, eyes closed, among golden sparkles"></div>
  <svg class="abs" style="left:182px;top:8px" width="14" height="10" viewBox="0 0 14 10" aria-hidden="true"><path d="M2 2l5 5 5-5" fill="none" stroke="#fff" stroke-width="2"/></svg>
  <h1 class="hero-title"><span class="l1">"Tapered Eyelashes"</span><span class="l2">With Human Hair</span></h1>
  <p class="hero-copy">New technology with tapered hair brand new with premium packaging handmade with premium hair comportable with natural and soft !<br>You look more perfect with Aurelle</p>
</section>

<div class="white-band"></div>

<div class="season" style="left:131px;background:linear-gradient(135deg,#f0a7b8,#e287a0 60%,#f2b9c2)" role="img" aria-label="Spring blossom backdrop"><div class="caption">Spring Special<br>Blossom Your Eyes</div></div>
<div class="season" style="left:365px;background:linear-gradient(135deg,#c43a86,#9c3b8e 55%,#d869a6)" role="img" aria-label="Fall petals backdrop"><div class="caption">Fall Special<br>Fascinating Your Eyes</div></div>
<div class="season" style="left:599px;background:linear-gradient(135deg,#7a3a1a,#5a2a14 60%,#8a4a22)" role="img" aria-label="Summer golden sparkle backdrop"><div class="caption">Summer Special<br>Sparkling Your Eyes</div></div>
<div class="season" style="left:833px;background:linear-gradient(135deg,#b9c6e8,#9fb1e0 60%,#c7d2ef)" role="img" aria-label="Winter frost backdrop"><div class="caption">Winner Special<br>Dazzling Your Eyes</div></div>

<div class="season-thumb" style="left:182px"><div role="img" aria-label="Close-up of a closed eye with a soft pink lash look" style="background:linear-gradient(180deg,#e9c9bc 0%,#cfa592 50%,#b8877a 62%,#e7c2b6 100%)"></div></div>
<div class="season-thumb" style="left:416px"><div role="img" aria-label="Close-up of a closed eye with a smoky lash look" style="background:linear-gradient(160deg,#9a7a7c 0%,#6d4f52 45%,#2e2024 62%,#b23a7c 100%)"></div></div>
<div class="season-thumb" style="left:650px"><div role="img" aria-label="Close-up of a closed eye with a golden lash look" style="background:linear-gradient(180deg,#c98b4a 0%,#e0aa62 45%,#f0cf8a 65%,#a06530 100%)"></div></div>
<div class="season-thumb" style="left:884px"><div role="img" aria-label="Close-up of a closed eye with a frosted lilac lash look" style="background:linear-gradient(180deg,#ecd6dc 0%,#d2aebf 45%,#7e6a86 62%,#e6d8e4 100%)"></div></div>

<div class="reviews-band"></div>

<div class="cart" style="left:229px"><svg width="18" height="16" viewBox="0 0 18 16" aria-hidden="true"><path d="M1 2h3l2 8h9l2-6H5" fill="none" stroke="#6b4530" stroke-width="1.6"/><circle cx="7" cy="13.5" r="1.4" fill="#6b4530"/><circle cx="14" cy="13.5" r="1.4" fill="#6b4530"/></svg></div>
<div class="cart" style="left:463px"><svg width="18" height="16" viewBox="0 0 18 16" aria-hidden="true"><path d="M1 2h3l2 8h9l2-6H5" fill="none" stroke="#6b4530" stroke-width="1.6"/><circle cx="7" cy="13.5" r="1.4" fill="#6b4530"/><circle cx="14" cy="13.5" r="1.4" fill="#6b4530"/></svg></div>
<div class="cart" style="left:697px"><svg width="18" height="16" viewBox="0 0 18 16" aria-hidden="true"><path d="M1 2h3l2 8h9l2-6H5" fill="none" stroke="#6b4530" stroke-width="1.6"/><circle cx="7" cy="13.5" r="1.4" fill="#6b4530"/><circle cx="14" cy="13.5" r="1.4" fill="#6b4530"/></svg></div>
<div class="cart" style="left:931px"><svg width="18" height="16" viewBox="0 0 18 16" aria-hidden="true"><path d="M1 2h3l2 8h9l2-6H5" fill="none" stroke="#6b4530" stroke-width="1.6"/><circle cx="7" cy="13.5" r="1.4" fill="#6b4530"/><circle cx="14" cy="13.5" r="1.4" fill="#6b4530"/></svg></div>

<div class="review-btn" style="left:172px">CHECK PRODUCT REVIEWS</div>
<div class="review-btn" style="left:409px">CHECK PRODUCT REVIEWS</div>
<div class="review-btn" style="left:643px">CHECK PRODUCT REVIEWS</div>
<div class="review-btn" style="left:877px">CHECK PRODUCT REVIEWS</div>

<footer class="site-footer">
  <div class="news-label">Sign Up For Newsletter</div>
  <div class="email">EMAIL ADDRESS</div>
  <div class="subscribe">SUBSCRIBE</div>
  <div class="follow">Follow Us On</div>
  <span class="social" style="left:932px" aria-label="Share">
    <svg width="14" height="14" viewBox="0 0 14 14" aria-hidden="true"><circle cx="3" cy="7" r="1.8" fill="#fff"/><circle cx="11" cy="3" r="1.8" fill="#fff"/><circle cx="11" cy="11" r="1.8" fill="#fff"/><path d="M3 7L11 3M3 7l8 4" stroke="#fff" stroke-width="1.2"/></svg>
  </span>
  <span class="social" style="left:968px" aria-label="Email">
    <svg width="14" height="12" viewBox="0 0 14 12" aria-hidden="true"><rect x="1" y="2" width="12" height="8.5" fill="none" stroke="#fff" stroke-width="1.4"/><path d="M1 2.5l6 4.5 6-4.5" fill="none" stroke="#fff" stroke-width="1.4"/></svg>
  </span>
  <span class="social" style="left:1004px" aria-label="Link">
    <svg width="14" height="14" viewBox="0 0 14 14" aria-hidden="true"><path d="M6 8.5L8.5 6M5.2 6.2L3.4 8a2.2 2.2 0 003.1 3.1l1.8-1.8M8.8 7.8L10.6 6a2.2 2.2 0 00-3.1-3.1L5.7 4.7" fill="none" stroke="#fff" stroke-width="1.5" stroke-linecap="round"/></svg>
  </span>
  <span class="social" style="left:1040px" aria-label="Favourite">
    <svg width="14" height="13" viewBox="0 0 14 13" aria-hidden="true"><path d="M7 12S1 8 1 4.3A3 3 0 017 3a3 3 0 016 1.3C13 8 7 12 7 12z" fill="#fff"/></svg>
  </span>
  <div class="rule"></div>
  <div class="copyright">Copyright 2015 Aurelle. All Right Reserved.</div>
</footer>

</body>
</html>
```